Business Cards for Demolition & Salvage Company

We are Licensed Demolition Contractors and this business card design is for our Salvage Yard. We recycle over 95% of the building materials removed from each demolition site in which we take to our Salvage Yard for resale eg. bricks, windows, doors, kitchens, stoves, lights, fencing etc so pretty much everything.
Updates

I forgot to note that single sided business card only please.

Project Deadline Extended
Reason: I would like to ask if designers could please submit or re-submit their designs edited to a single sided card only. The card also does not need space for an employee name or position as our general business contact details will suffice for this project. Primary colour must be ROYAL BLUE with no exceptions please. Much appreciated and thank you to all whom have submitted designs to date and I look forward to receiving your edited designs..

Industry/Entity Type

Building

Contact Information for Business Card

Fendrell Demolition & Salvage (WA) Pty Ltd
2437 Old Quarry Parade
UPPER MARLOW WA 6071
P: (08) 9471 3058
F: (08) 9471 2267
E: salvage@fdwreck.com.au
W: fendrelldemolition.com.au

Requirements
Must have
• We have a logo that has been with our Company since 1974 so he must be included in the design - file attached. As for colours, we have always used royal blue and again this must be the primary colour used in the design. Please keep the design simple.
Nice to have
• Card can include opening hours as follows:
Opening Hours:
Monday to Friday 8am - 5.00pm
Saturday 8am - 3pm
Closed Sunday's and public holidays

```html
<!DOCTYPE html>
<html lang="en">
<head>
<meta charset="utf-8">
<title>Fendrell Demolition &amp; Salvage – Business Card</title>
<link href="https://fonts.googleapis.com/css2?family=Lato:wght@400;700;900&display=swap" rel="stylesheet">
<style>
  :root {
    --royal: #283593;
    --navy-ink: #1b1d4d;
    --ink: #1e1e1e;
    --paper: #ffffff;
    --paper-shade: #eef0f3;
    --stage: #2b2b2b;
    --recycle-green: #6fbf3a;
    --logo-tone: #3d5bb0;
  }
  * { box-sizing: border-box; margin: 0; padding: 0; }
  html, body {
    width: 1200px; height: 997px; overflow: hidden;
    background: var(--stage);
    font-family: "Lato", sans-serif;
  }
  .card {
    position: absolute; left: 150px; top: 241px;
    width: 900px; height: 514px;
    background: linear-gradient(135deg, var(--paper) 55%, var(--paper-shade));
    border-radius: 34px; overflow: hidden;
    color: var(--ink);
  }
  .brand-mark {
    position: absolute; left: 60px; top: 40px;
    width: 150px; height: 150px; border-radius: 50%;
    background: radial-gradient(circle at 40% 40%, #6d86cf, var(--logo-tone));
  }
  .brand-name {
    position: absolute; left: 232px; top: 70px;
    font-weight: 900; font-size: 39px; line-height: 1.05;
    color: var(--navy-ink); text-transform: uppercase; letter-spacing: 0.5px;
  }
  .licence-pill {
    position: absolute; left: 240px; top: 168px;
    background: var(--royal); color: var(--paper);
    font-weight: 700; font-size: 19px; letter-spacing: 0.6px;
    padding: 4px 18px; border-radius: 16px; text-transform: uppercase;
  }
  .contact-rail {
    position: absolute; left: 0; top: 262px;
    width: 62px; height: 218px;
    background: var(--royal); border-radius: 0 22px 22px 0;
    display: flex; flex-direction: column; justify-content: space-around;
    align-items: center; padding: 10px 0;
  }
  .contact-rail svg { width: 24px; height: 24px; fill: var(--paper); }
  .contact-list {
    position: absolute; left: 86px; top: 268px;
    list-style: none; font-weight: 700; font-size: 21px; line-height: 41px;
  }
  .contact-list .address { line-height: 26px; padding-top: 8px; }
  .recycle-badge {
    position: absolute; left: 420px; top: 300px;
    width: 84px; height: 84px; border-radius: 50%;
    background: var(--recycle-green);
  }
  .hours-band {
    position: absolute; right: 0; top: 218px;
    width: 330px; height: 22px; background: var(--royal);
    border-radius: 11px 0 0 11px;
  }
  .hours-title {
    position: absolute; left: 515px; top: 238px;
    background: var(--royal); color: var(--paper);
    font-weight: 900; font-size: 24px; text-transform: uppercase;
    padding: 3px 18px; border-radius: 18px;
  }
  .hours-text {
    position: absolute; right: 40px; top: 285px;
    text-align: right; font-weight: 700; font-size: 21px; line-height: 34px;
  }
  .closed-band {
    position: absolute; right: 0; top: 378px;
    width: 390px; height: 36px; background: var(--royal);
    color: var(--paper); font-weight: 700; font-size: 21px;
    border-radius: 18px 0 0 18px; padding: 5px 0 0 28px;
  }
</style>
</head>
<body>
  <main class="card">
    <div class="brand-mark" role="img" aria-label="Company mascot logo area"></div>
    <h1 class="brand-name">Fendrell Demolition<br>&amp; Salvage (WA) Pty Ltd</h1>
    <p class="licence-pill">Licensed Demolition Contractors</p>

    <div class="contact-rail" aria-hidden="true">
      <svg viewBox="0 0 24 24"><path d="M6.6 10.8a15 15 0 0 0 6.6 6.6l2.2-2.2c.3-.3.7-.4 1-.2 1.1.4 2.3.6 3.6.6.6 0 1 .4 1 1V20c0 .6-.4 1-1 1A17 17 0 0 1 3 4c0-.6.4-1 1-1h3.5c.6 0 1 .4 1 1 0 1.3.2 2.5.6 3.6.1.3 0 .7-.2 1z"/></svg>
      <svg viewBox="0 0 24 24"><path d="M6 2h10l2 2v5H6zM3 10h18c1 0 2 1 2 2v6h-4v4H5v-4H1v-6c0-1 1-2 2-2zm4 7v3h10v-3z"/></svg>
      <svg viewBox="0 0 24 24"><path d="M2 5h20v14H2zm2 2v.5l8 5.5 8-5.5V7zm0 3v7h16v-7l-8 5.5z"/></svg>
      <svg viewBox="0 0 24 24"><path d="M10.6 13.4a1 1 0 0 1 0-1.4l3-3a1 1 0 1 1 1.4 1.4l-3 3a1 1 0 0 1-1.4 0zM8 11l-3 3a3 3 0 0 0 4.2 4.2l3-3 1.4 1.4-3 3A5 5 0 1 1 3.6 12.6l3-3zm8 2 3-3A3 3 0 0 0 14.8 5.8l-3 3-1.4-1.4 3-3a5 5 0 1 1 7 7l-3 3z"/></svg>
      <svg viewBox="0 0 24 24"><path d="M12 2a7 7 0 0 0-7 7c0 5 7 13 7 13s7-8 7-13a7 7 0 0 0-7-7zm0 9.5A2.5 2.5 0 1 1 12 6.5a2.5 2.5 0 0 1 0 5z"/></svg>
    </div>
    <ul class="contact-list">
      <li>(08) 9471 3058</li>
      <li>(08) 9471 2267</li>
      <li>salvage@fdwreck.com.au</li>
      <li>fendrelldemolition.com.au</li>
      <li class="address">Old Quarry Parade,<br>Upper Marlow WA 6071</li>
    </ul>

    <div class="recycle-badge" role="img" aria-label="Recycling guarantee badge"></div>

    <div class="hours-band"></div>
    <h2 class="hours-title">Opening Hours:</h2>
    <p class="hours-text">Mon - Fri 8:00 AM - 5:00PM,<br>Sat 8am - 3pm</p>
    <p class="closed-band">Closed Sunday's &amp; Public Holidays</p>
  </main>
</body>
</html>
```